Design website home page for pathology consulting company

Starting a new consulting company with anatomic pathologists focused on expert diagnosis and second opinions on difficult pathology cases. In the near future we will be incorporating next generation diagnostics for rare diseases of childhood into the business. These include discovery and testing of DNA for mutations.

The company is formed around one of the best known pathologists in the world named Harold "Juniper" Tolvik. The name of the company is "JuniperLab"

We had a logo design by ArtfulHive - it is great. I will attach file as soon as I have it (contest ending today). Our company is medical, uses microscopes, DNA, probably will focus on childhood diseases but not solely on childhood diseases. we're not particularly conservative, but the customers we want to appeal to include older practicing pathologists as well as patients (sometimes parents) looking for second opinions.

Think a group of expert doctors diagnosing disease through the microscope and through DNA technology, ages ranging from 35-75 all trained by the best pathologist in the world - "Juniper"

We receive glass slides from diseases from patients all over the world from docs who need an expert to tell them what is the diagnosis. So "path to the diagnosis" is also part of the company marketing message.

We want the website design to describe our company but be very simple to find what one is looking for as we will use it as the launch page to:
1) order services
2) check results/reports
3) set up new account
4) speak with one of the pathologists
5) see our test menu
6) access our educational material/webinars
Updates

Update - looking for home page design and then finalists will ask for second page design to keep with theme - ok?

Reason: realized this project isn't web design but web home page design - thanks

Reason: Holidays for some in next two weeks

Reason: Hot discussion among collaborators for a few of the submissions. Will provide detail individually this weekend. Thanks so much for all the submissions!

Target Market(s)

Referring pathologists, physicians who want second opinions on pathology disease diagnosis, patients who have had biopsies (either patients themselves or parents of patients), generally high education level

Industry/Entity Type

Marketing

Requirements
Must have
• JuniperLab
Next Generation Pathology Consultants

```html
<!DOCTYPE html>
<html lang="en">
<head>
<meta charset="utf-8">
<title>JuniperLab – Next Generation Pathology Consultants</title>
<link href="https://fonts.googleapis.com/css2?family=Lora:wght@400;700&family=Roboto:wght@400;500;700&family=Open+Sans:wght@400;600;700&display=swap" rel="stylesheet">
<style>
:root{
  --blue:#0b5eb0;
  --blue-dark:#0a4f96;
  --text:#333;
  --muted:#777;
  --panel:#d6d6d6;
  --footer:#929396;
  --footer-bottom:#5e5f62;
  --gold:#f6c23e;
}
*{margin:0;padding:0;box-sizing:border-box}
html,body{width:1108px;height:1200px;overflow:hidden;background:#fff}
.stage{position:relative;width:1200px;height:1300px;transform:scale(.9234);transform-origin:0 0;font-family:"Open Sans",sans-serif;color:var(--text)}
.page{position:absolute;left:189px;top:0;width:823px;height:1300px;background:#fbfbfb}
.abs{position:absolute}
.topline{left:0;top:0;width:823px;height:3px;background:var(--blue)}
.account-tab{left:497px;top:0;width:232px;height:22px;background:var(--blue);color:#fff;font:500 9.5px "Roboto",sans-serif;display:flex;justify-content:center;align-items:center;gap:14px;clip-path:polygon(0 0,100% 0,97% 100%,3% 100%)}
.logo{left:100px;top:14px;width:104px;text-align:center}
.logo-mark{display:block;margin:0 auto 2px;width:44px;height:44px;border-radius:50%;background:#8a8d92}
.logo-name{font:400 16px "Lora",serif;color:var(--blue);font-variant:small-caps;letter-spacing:.3px}
.logo-tag{font:400 5.5px "Open Sans",sans-serif;color:#666;white-space:nowrap}
.contact{left:362px;top:41px;font:400 9px "Roboto",sans-serif;color:#888;display:flex;gap:14px;align-items:center}
.contact span{display:flex;gap:4px;align-items:center}
.nav{left:339px;top:65px;font:500 8.5px "Roboto",sans-serif;color:var(--blue);display:flex;gap:14px}
.nav i{font-style:normal;color:var(--blue)}
.hero{left:0;top:90px;width:823px;height:391px;background:linear-gradient(90deg,#e8edf1 0%,#dfe7ec 35%,#b9c6cf 60%,#8ea4b3 80%,#c9d3da 100%)}
.hero-title{left:103px;top:172px;font:400 31px/1.05 "Lora",serif;color:var(--blue);font-variant:small-caps}
.hero-text{left:105px;top:250px;width:300px;font:400 12px/17px "Roboto",sans-serif;color:#666}
.consult{left:73px;top:411px;width:668px;height:149px;background:linear-gradient(#e6e8eb,#b7babf)}
.consult h2{position:absolute;left:29px;top:20px;font:400 16.5px/20px "Lora",serif;color:var(--blue);text-transform:uppercase}
.consult p{position:absolute;left:29px;top:70px;width:185px;font:400 8px/12.5px "Open Sans",sans-serif;color:#333}
.divider{position:absolute;left:243px;top:12px;width:1px;height:118px;background:#9ea2a7}
.field{position:absolute;height:22px;background:#eee;border:1px solid #c8c8c8;font:400 7.5px "Open Sans",sans-serif;color:#777;padding:6px 8px}
.send{position:absolute;left:276px;top:108px;width:110px;height:25px;background:linear-gradient(#fdd868,#f1b52c);font:600 11px "Open Sans",sans-serif;color:#333;display:flex;align-items:center;justify-content:center;letter-spacing:.3px}
.card{position:absolute;top:586px;width:212px}
.card h3{font:400 16.5px "Lora",serif;color:var(--blue);margin-bottom:7px}
.card .photo{height:90px}
.card p{margin:16px 2px 0;font:400 8px/12.5px "Open Sans",sans-serif;color:#333}
.card a{display:block;margin:13px 2px 0;font:700 8px "Open Sans",sans-serif;color:var(--blue);text-decoration:underline}
.testimonials{left:0;top:815px;width:823px;height:171px;background:var(--panel)}
.section-title{font:400 17px "Lora",serif;color:var(--blue);text-align:center}
.clients-title{z-index:2;line-height:20px}
.quote{position:absolute;top:63px;width:190px;font:400 10.5px/15px "Open Sans",sans-serif;color:#777}
.quote b{display:block;margin-top:15px;font:600 10px "Open Sans",sans-serif;color:#666}
.client{position:absolute;z-index:1;background:#fff;display:flex;align-items:center;justify-content:center;gap:6px;font:700 17px "Open Sans",sans-serif;color:#8e8e8e}
.client .dot{width:14px;height:14px;border-radius:50%;background:#a9a9a9}
.client-line{position:absolute;top:1083px;height:1px;background:#ddd}
.footer{left:0;top:1133px;width:823px;height:119px;background:var(--footer)}
.footer-col{position:absolute;top:20px;font:400 8px/16.5px "Open Sans",sans-serif;color:#f2f2f2}
.footer-col .head{color:#b9bbbe;letter-spacing:.3px}
.footer .logo-name{color:#5a5c60;font-size:19px}
.footer .logo-tag{color:#55575b;font-size:6.5px}
.footer .logo-mark{width:54px;height:54px;background:#6f7176}
.bottom{left:0;top:1252px;width:823px;height:48px;background:var(--footer-bottom);border-top:2px solid #4d4e51;color:#d6d6d6;font:400 8.5px "Open Sans",sans-serif;display:flex;align-items:center;justify-content:center}
</style>
</head>
<body>
<div class="stage">
 <div class="page">
  <div class="abs topline"></div>
  <div class="abs account-tab"><span>Check Result</span><span>|</span><span>Login</span><span>|</span><span>Register</span></div>

  <div class="abs logo">
   <span class="logo-mark"></span>
   <div class="logo-name">JuniperLab</div>
   <div class="logo-tag">Next Generation Pathology Consultants</div>
  </div>

  <div class="abs contact">
   <span><svg width="11" height="8" viewBox="0 0 11 8"><rect x=".5" y=".5" width="10" height="7" fill="none" stroke="#999"/><path d="M.5 .5l5 4 5-4" fill="none" stroke="#999"/></svg>info@juniperlab.com</span>
   <span><svg width="10" height="10" viewBox="0 0 10 10"><circle cx="5" cy="5" r="4.3" fill="none" stroke="#999"/><path d="M5 2.5V5h2" fill="none" stroke="#999"/></svg>Monday-Friday: 8:00am-5:00pm</span>
   <span><svg width="11" height="11" viewBox="0 0 11 11"><path d="M2 1l2 2.5-1 1.2c.8 1.6 1.8 2.6 3.3 3.3l1.2-1 2.5 2-1.3 1.5C5 10 1 6 .7 2.3z" fill="none" stroke="#999"/></svg>+1800 555 0142</span>
  </div>
  <div class="abs nav"><span>ORDER SERVICES</span><i>|</i><span>TEST MENU</span><i>|</i><span>WEBINARS</span><i>|</i><span>ABOUT</span><i>|</i><span>CONTACT US</span></div>

  <div class="abs hero" role="img" aria-label="Two pathologists in lab coats reviewing notes in a bright laboratory"></div>
  <h1 class="abs hero-title">Expert Disease<br>Diagnosis</h1>
  <p class="abs hero-text">Lorem ipsum dolor sit amet, consectetur adipisicing elit, sed do eiusmod tempor incididunt ut labore et dolore magna aliqua.</p>

  <div class="abs consult">
   <h2>Consult with one<br>of the pathologists</h2>
   <p>Lorem ipsum dolor sit amet, consectetur adipisicing elit, sed do eiusmod tempor incididunt ut labore et dolore magna aliqua.</p>
   <div class="divider"></div>
   <div class="field" style="left:276px;top:15px;width:110px">Enter your name..</div>
   <div class="field" style="left:393px;top:15px;width:110px">Enter your email..</div>
   <div class="field" style="left:508px;top:15px;width:110px">Enter your phone..</div>
   <div class="field" style="left:276px;top:46px;width:343px;height:54px">Enter your message..</div>
   <div class="send">SEND EMAIL</div>
  </div>

  <div class="card" style="left:81px">
   <h3>Our Services</h3>
   <div class="photo" role="img" aria-label="Scientist with pipette working at a lab bench" style="background:linear-gradient(90deg,#9fc3e0,#4f8fc9 60%,#2d6eaf)"></div>
   <p>Lorem ipsum dolor sit amet, consectetur adipisicing elit, sed do eiusmod tempor incididunt ut labore et dolore magna aliqua. Ut enim ad minim veniam, quis nostrud exercitation.</p>
   <a>READ MORE</a>
  </div>
  <div class="card" style="left:308px;width:205px">
   <h3>Test Menu</h3>
   <div class="photo" role="img" aria-label="Row of test tubes filled with blue and orange liquid" style="background:linear-gradient(90deg,#5f8fd8,#f0a24a 45%,#4d7fe0 70%,#e88f3a)"></div>
   <p>Lorem ipsum dolor sit amet, consectetur adipisicing elit, sed do eiusmod tempor incididunt ut labore et dolore magna aliqua. Ut enim ad minim veniam, quis nostrud exercitation.</p>
   <a>READ MORE</a>
  </div>
  <div class="card" style="left:527px">
   <h3>Educational Webinars</h3>
   <div class="photo" role="img" aria-label="Brain scan graphic beside a doctor in a surgical mask" style="background:linear-gradient(90deg,#bcd9df,#d9eaee 50%,#eef3f4)"></div>
   <p>Lorem ipsum dolor sit amet, consectetur adipisicing elit, sed do eiusmod tempor incididunt ut labore et dolore magna aliqua. Ut enim ad minim veniam, quis nostrud exercitation.</p>
   <a>READ MORE</a>
  </div>

  <div class="abs testimonials">
   <h2 class="section-title" style="margin-top:28px">Testimonials</h2>
   <div class="quote" style="left:90px">“It’s a pleasure dealing with such professional organisations.”<b>Dana Reyes, Northfield Clinic</b></div>
   <div class="quote" style="left:309px;width:216px">“I like your creed, service is so important. As I’ve seen it in action I know its true.”<b>Marcus Hale, Brightwell Labs</b></div>
   <div class="quote" style="left:528px;width:205px">“Expert diagnosis. Trusted organization. Recommended to all.”<b>Priya Nandan, Solace Health</b></div>
  </div>

  <div class="client-line" style="left:240px;width:14px"></div>
  <div class="client-line" style="left:405px;width:14px"></div>
  <div class="client-line" style="left:570px;width:30px"></div>
  <div class="client-line" style="left:720px;width:14px"></div>
  <div class="client" style="left:89px;top:1013px;width:151px;height:113px"><span class="dot"></span>Harborline</div>
  <div class="client" style="left:254px;top:1013px;width:151px;height:113px">Vextra</div>
  <div class="client" style="left:419px;top:1013px;width:151px;height:113px">Calmora</div>
  <div class="client" style="left:600px;top:1026px;width:120px;height:88px">Orvane</div>
  <h2 class="abs section-title clients-title" style="left:0;top:1003px;width:823px">Some of Our Clients</h2>

  <div class="abs footer">
   <div class="logo" style="position:absolute;left:90px;top:20px;width:116px;text-align:center">
    <span class="logo-mark"></span>
    <div class="logo-name">JuniperLab</div>
    <div class="logo-tag">Next Generation Pathology Consultants</div>
   </div>
   <div class="footer-col" style="left:306px"><div class="head">NAVIGATION</div>Home<br>Order Services<br>Testu Menu<br>Webinars</div>
   <div class="footer-col" style="left:434px"><div class="head">ABOUT US</div>Login<br>Register<br>Check Results<br>Contact Us</div>
   <div class="footer-col" style="left:558px"><div class="head">CONTACT US</div>Phone : +61 3 555 0198<br>Email: info@juniperlab.com<br>Your Street, Your Avenue<br>Your Country, 10001</div>
  </div>
  <div class="abs bottom">© Copyright 2013 JuniperLab. All Right Reserved | Privacy Policy | Site Map</div>
 </div>
</div>
</body>
</html>
```